Design Shopify E-Commerce Website for Men's Products

Design a Shopify website for men to sell our men's jewelry, cigar and bar accessories, and other men's products. Design should be hip, with like a rock n' roll, biker, whiskey driker flare. Name of the company is "Ironvale Locker" and website will be www.IronvaleLocker.com
Homepage will have navigation bar with three categories: Men's Jewelry, Cigar & Bar Products, Man Cave Swag
I will upload our logo, inspiration type pictures and some of the products that we sell
Theme colors should be mainly dark: black, grey, brown, gold

```html
<!DOCTYPE html>
<html lang="en">
<head>
<meta charset="utf-8">
<title>Ironvale Locker — Men's Products</title>
<link rel="stylesheet" href="https://fonts.googleapis.com/css2?family=Poppins:ital,wght@0,400;0,500;0,600;0,700;1,400&display=swap">
<style>
:root{
  --gold:#d4a12a;
  --gold-deep:#c0901f;
  --black:#000;
  --ink:#1d1d1d;
  --body:#333;
  --cream:#f2ece1;
  --cream-soft:#faf4e6;
  --blog-bg:#fdfaf2;
  --dark:#231f20;
  --footer:#1b1919;
  --white:#fff;
}
*{box-sizing:border-box;margin:0;padding:0}
html,body{width:1200px;height:4127px;overflow:hidden}
body{position:relative;font-family:'Poppins',sans-serif;color:var(--ink);background:var(--white)}
.abs{position:absolute}
.center{text-align:center}
.eyebrow{font-size:16px;color:var(--gold);text-transform:uppercase;letter-spacing:.5px}
.heading{font-size:34px;font-weight:700;text-transform:uppercase;letter-spacing:1px;color:var(--ink)}
.btn{position:absolute;display:flex;align-items:center;justify-content:center;font-size:10px;font-weight:600;text-transform:uppercase;letter-spacing:.5px}
.btn-gold{background:var(--gold);color:var(--white)}
.btn-outline{border:1.5px solid var(--gold);color:var(--gold);background:var(--white)}
.photo{position:absolute}

/* header */
.site-header{position:absolute;left:0;top:0;width:1200px;height:101px;background:var(--black)}
.brand{position:absolute;left:100px;top:38px;display:flex;align-items:center;gap:8px;color:var(--gold);font-weight:600;font-size:16px}
.brand .dot{width:12px;height:12px;border-radius:50%;background:var(--gold)}
.main-nav a{position:absolute;top:46px;color:var(--white);font-size:11px;font-weight:500;letter-spacing:.6px;text-decoration:none}

/* hero */
.hero{position:absolute;left:0;top:101px;width:1200px;height:588px;background:var(--cream);overflow:hidden}

/* products */
.product{position:absolute;width:240px;text-align:center}
.product-name{font-size:18px;font-weight:500;color:var(--gold)}
.product-desc{font-size:11px;color:#555;line-height:1.2;margin-top:6px}
.product-price{font-size:16px;font-weight:600;margin-top:8px}

/* features */
.features{position:absolute;left:0;top:1291px;width:1200px;height:59px;background:var(--cream-soft)}
.feature{position:absolute;top:18px;display:flex;align-items:center;gap:14px;font-size:15px;font-weight:500;letter-spacing:.5px}

/* text blocks */
.copy{font-size:13px;line-height:20px;color:var(--body)}
.jewelry{position:absolute;left:0;top:1927px;width:1200px;height:526px;background:linear-gradient(90deg,#c4951f,#dfad2d)}
.jewelry .copy{color:var(--white)}

/* blogs */
.blogs{position:absolute;left:0;top:2453px;width:1200px;height:604px;background:var(--blog-bg)}
.blog-card{position:absolute;top:131px;width:296px;height:401px;background:var(--white);border:1px solid #ecd9a8;border-radius:4px;overflow:hidden}
.blog-card .photo{left:0;top:0;width:100%;height:213px}
.blog-body{position:absolute;left:25px;top:240px;right:20px}
.blog-title{font-size:14px;font-weight:600;line-height:18px}
.blog-text{font-size:11.5px;line-height:19px;color:#444;margin-top:10px}
.blog-link{font-size:11px;color:var(--gold);text-decoration:underline;margin-top:6px;display:block}

/* newsletter */
.newsletter{position:absolute;left:0;top:3558px;width:1200px;height:155px;background:var(--dark)}
.footer{position:absolute;left:0;top:3713px;width:1200px;height:414px;background:var(--footer);color:var(--white)}
.footer h4{font-size:16px;font-weight:500;letter-spacing:1px;text-transform:uppercase}
.footer ul{list-style:none;margin-top:18px;font-size:12px;line-height:19px;color:#ddd}
.social{position:absolute;top:228px;width:30px;height:30px;border-radius:50%;background:var(--gold)}
</style>
</head>
<body>

<header class="site-header">
  <div class="brand"><span class="dot"></span>Ironvale Locker</div>
  <nav class="main-nav">
    <a style="left:352px">MEN'S JEWELRY</a>
    <a style="left:523px">CIGAR &amp; BAR PRODUCTS</a>
    <a style="left:736px">MAN CAVE SWAG</a>
  </nav>
  <svg class="abs" style="left:977px;top:44px" width="120" height="24" fill="none" stroke="#d4a12a" stroke-width="1.6">
    <circle cx="10" cy="10" r="7"/><line x1="15" y1="15" x2="20" y2="20"/>
    <circle cx="61" cy="12" r="10"/><circle cx="61" cy="9" r="3.5"/><path d="M54 19c2-4 12-4 14 0"/>
    <path d="M99 8h14l-1.5 13h-11z"/><path d="M102 8c0-6 8-6 8 0"/>
  </svg>
</header>

<section class="hero">
  <svg class="abs" style="left:111px;top:66px" width="450" height="450"><circle cx="225" cy="225" r="224" fill="none" stroke="#d4a12a" stroke-width="1.5"/><circle cx="225" cy="225" r="214" fill="#fff"/></svg>
  <div class="abs center" style="left:136px;top:220px;width:400px">
    <div style="font-size:30px;font-weight:700;color:var(--gold);line-height:34px;letter-spacing:1px">WELCOME TO<br>IRONVALE LOCKER</div>
    <p style="font-size:12.5px;line-height:19px;margin-top:10px;color:#222">Lorem ipsum dolor sit amet, consectetur adipisc-<br>ing elit, sed do eiusmod</p>
  </div>
  <div class="btn btn-gold" style="left:274px;top:357px;width:125px;height:32px">Buy Now</div>
  <div class="photo" role="img" aria-label="Open wooden cigar humidor with cigars" style="left:261px;top:428px;width:159px;height:160px;background:linear-gradient(160deg,#c07a3a,#7a3d14);border-radius:6px"></div>
  <div class="photo" role="img" aria-label="Man with locs smoking, wearing a maroon t-shirt" style="left:649px;top:88px;width:408px;height:500px;background:linear-gradient(180deg,#3a2a24,#6b3540 60%,#5a2a35);border-radius:180px 180px 0 0"></div>
</section>

<section>
  <div class="abs center eyebrow" style="left:0;top:744px;width:1178px">Products</div>
  <h2 class="abs center heading" style="left:0;top:764px;width:1200px">Men's Products</h2>
  <div class="abs" style="left:352px;top:860px;width:247px;height:378px;background:#fff;box-shadow:0 2px 14px rgba(0,0,0,.12)"></div>
  <svg class="abs" style="left:62px;top:1012px" width="24" height="44" fill="none" stroke="#555" stroke-width="2"><path d="M22 2 2 22l20 20"/></svg>
  <svg class="abs" style="left:1106px;top:1012px" width="24" height="44" fill="none" stroke="#555" stroke-width="2"><path d="M2 2l20 20L2 42"/></svg>

  <div class="product" style="left:101px;top:913px">
    <div role="img" aria-label="Red lacquered cigar humidor" style="margin:0 auto;width:160px;height:136px;background:linear-gradient(160deg,#a52a2a,#5a1010);border-radius:8px"></div>
    <div class="product-name" style="margin-top:20px">Cigar</div>
    <div class="product-desc">Lorem ipsum dolor sit amet,<br>consectetur adipiscing</div>
    <div class="product-price">$15.87</div>
  </div>
  <div class="btn btn-outline" style="left:158px;top:1161px;width:127px;height:34px">Buy Now</div>

  <div class="product" style="left:349px;top:913px">
    <div role="img" aria-label="Octagonal cigar ashtray" style="margin:0 auto;width:170px;height:136px;background:linear-gradient(180deg,#8a8a8a,#5a1a1a 55%);border-radius:40%"></div>
    <div class="product-name" style="margin-top:20px">Cigar Astray</div>
    <div class="product-desc">Lorem ipsum dolor sit amet,<br>consectetur adipiscing</div>
    <div class="product-price">$19.87</div>
  </div>
  <div class="btn btn-outline" style="left:406px;top:1161px;width:127px;height:34px">Buy Now</div>

  <div class="product" style="left:606px;top:913px">
    <div role="img" aria-label="Silver cross pendant" style="margin:0 auto;width:130px;height:136px;background:linear-gradient(135deg,#e6e6e6,#7a7a7a);border-radius:12px"></div>
    <div class="product-name" style="margin-top:20px">Pendant</div>
    <div class="product-desc">Lorem ipsum dolor sit amet,<br>consectetur adipiscing</div>
    <div class="product-price">$24.87</div>
  </div>
  <div class="btn btn-outline" style="left:663px;top:1161px;width:127px;height:34px">Buy Now</div>

  <div class="product" style="left:856px;top:913px">
    <div role="img" aria-label="Silver fleur ring" style="margin:0 auto;width:110px;height:110px;background:radial-gradient(circle,#f2f2f2,#6e6e6e);border-radius:50%"></div>
    <div class="product-name" style="margin-top:46px">Cigar</div>
    <div class="product-desc">Lorem ipsum dolor sit amet,<br>consectetur adipiscing</div>
    <div class="product-price">$5.87</div>
  </div>
  <div class="btn btn-outline" style="left:913px;top:1161px;width:127px;height:34px">Buy Now</div>
</section>

<section class="features">
  <div class="feature" style="left:248px"><svg width="38" height="26" fill="none" stroke="#d4a12a" stroke-width="1.6"><rect x="2" y="3" width="30" height="19" rx="2"/><line x1="2" y1="9" x2="32" y2="9"/><line x1="7" y1="16" x2="16" y2="16"/></svg>PAY ONLINE</div>
  <div class="feature" style="left:548px"><svg width="28" height="30" fill="none" stroke="#d4a12a" stroke-width="1.6"><rect x="6" y="2" width="16" height="22" rx="2"/><line x1="10" y1="8" x2="18" y2="8"/><line x1="10" y1="13" x2="18" y2="13"/><line x1="14" y1="24" x2="14" y2="29"/></svg>BUY NOW</div>
  <div class="feature" style="left:849px"><svg width="32" height="26" fill="none" stroke="#d4a12a" stroke-width="1.6"><rect x="2" y="5" width="18" height="14"/><path d="M20 9h6l4 5v5H20z"/><circle cx="8" cy="21" r="3"/><circle cx="25" cy="21" r="3"/></svg>DELIVERED</div>
</section>

<section>
  <svg class="abs" style="left:136px;top:1421px" width="432" height="432"><circle cx="216" cy="216" r="215" fill="none" stroke="#d4a12a" stroke-width="1.5"/></svg>
  <div class="photo" role="img" aria-label="Man in a blue suit with cigar, ashtray and whiskey glasses" style="left:149px;top:1434px;width:406px;height:406px;border-radius:50%;background:linear-gradient(135deg,#8f7a66,#2d3f6e 55%,#b68648)"></div>
  <div class="abs eyebrow" style="left:609px;top:1499px;font-size:15px">Who we are</div>
  <h2 class="abs heading" style="left:609px;top:1522px;font-size:27px">About Ironvale Locker</h2>
  <div class="abs copy" style="left:614px;top:1573px;width:440px">
    <p>Lorem ipsum dolor sit amet, consectetur adipiscing elit, sed do eiusmod</p>
    <p style="margin-top:4px">tempor incididunt ut labore et dolore magna aliqua.</p>
    <p style="margin-top:4px">Quis ipsum suspendisse ultrices gravida. Risus commodo viver-ra maecenas accumsan lacus vel facilisis. Quis ipsum sus-pendisse ultrices gravida. Risus commodo viverra maecenas ac-cumsan lacus vel facilisis.</p>
  </div>
  <div class="btn btn-gold" style="left:617px;top:1738px;width:138px;height:34px">Learn More</div>
</section>

<section class="jewelry">
  <div class="abs" style="left:144px;top:132px;font-size:16px;color:#fff;letter-spacing:.5px">PRODUCT</div>
  <h2 class="abs heading" style="left:144px;top:152px;font-size:31px;color:#fff">Men's Jewelry</h2>
  <div class="abs copy" style="left:145px;top:198px;width:430px">
    <p>Lorem ipsum dolor sit amet, consectetur adipiscing elit, sed do eiusmod tempor incididunt ut labore et dolore magna aliqua.</p>
    <p style="margin-top:4px">Quis ipsum suspendisse ultrices gravida. Risus commodo viver-ra maecenas accumsan lacus vel facilisis. Quis ipsum sus-pendisse ultrices gravida. Risus commodo viverra maecenas ac-cumsan lacus vel facilisis. Risus commodo viverra maecenas ac-cumsan lacus vel facilisis.</p>
  </div>
  <div class="btn" style="left:144px;top:362px;width:138px;height:34px;background:#000;color:#fff">Learn More</div>
  <div class="photo" role="img" aria-label="Silver rings, chains and cross pendant on a wooden surface" style="left:638px;top:58px;width:406px;height:406px;border-radius:50%;background:radial-gradient(circle at 40% 40%,#b8743a,#6e3d1c)"></div>
</section>

<section class="blogs">
  <div class="abs center eyebrow" style="left:0;top:49px;width:1200px">Blogs</div>
  <h2 class="abs center heading" style="left:0;top:69px;width:1200px;font-size:31px">Featured Blogs</h2>

  <article class="blog-card" style="left:143px">
    <div class="photo" role="img" aria-label="Cigar beside a glass of whiskey on dark wood" style="background:linear-gradient(135deg,#3b2515,#7a4a22)"></div>
    <div class="blog-body">
      <div class="blog-title">The Harbor Stone Club Chair-<br>man's Annual Letter</div>
      <p class="blog-text">It is my great pleasure to be writing to you as the Harbor Stone Club is about to enter its 23rd year.</p>
      <a class="blog-link">LEARN MORE</a>
    </div>
  </article>
  <article class="blog-card" style="left:452px">
    <div class="photo" role="img" aria-label="Hands fastening a cufflink on a white shirt cuff" style="background:linear-gradient(135deg,#2a2a2a,#d8d4cc 60%,#1e1e1e)"></div>
    <div class="blog-body">
      <div class="blog-title">Congratulations Rowan<br>Hale</div>
      <p class="blog-text">The Harbor Stone Club wishes to congratulate our co-patron Rowan Hale on his elevation.</p>
      <a class="blog-link">LEARN MORE</a>
    </div>
  </article>
  <article class="blog-card" style="left:759px">
    <div class="photo" role="img" aria-label="Wooden whiskey gift box with glasses and stones" style="background:linear-gradient(135deg,#8a5a32,#c8c2b8)"></div>
    <div class="blog-body">
      <div class="blog-title">Harbor Stone Club<br>update from the Chair</div>
      <p class="blog-text">Dear sponsors, partners, members and friends,<br>I am writing to update you on activities</p>
      <a class="blog-link">LEARN MORE</a>
    </div>
  </article>
</section>

<section>
  <div class="abs center eyebrow" style="left:0;top:3116px;width:1220px">Reviews</div>
  <h2 class="abs center heading" style="left:0;top:3136px;width:1200px;font-size:31px">Testimonials</h2>
  <div class="abs" style="left:248px;top:3233px;width:731px;height:243px;border:1.5px solid var(--gold)"></div>
  <div class="abs" style="left:234px;top:3217px;width:732px;height:243px;background:#fff;box-shadow:0 2px 16px rgba(0,0,0,.1)"></div>
  <div class="photo" role="img" aria-label="Reviewer portrait" style="left:556px;top:3239px;width:86px;height:86px;border-radius:50%;background:linear-gradient(135deg,#1a1a1a,#8a2020)"></div>
  <svg class="abs" style="left:153px;top:3320px" width="24" height="52" fill="none" stroke="#777" stroke-width="1.6"><path d="M22 2 2 26l20 24"/></svg>
  <svg class="abs" style="left:1027px;top:3320px" width="24" height="52" fill="none" stroke="#777" stroke-width="1.6"><path d="M2 2l20 24L2 50"/></svg>
  <p class="abs center" style="left:355px;top:3336px;width:490px;font-size:11.5px;font-style:italic;line-height:19px;color:#666"><span style="font-size:20px;color:#888">“</span> Morbi diam mauris viverra in gravida eu mattis in ante Morbi eget arcu Morbi porta libero id ullamcorper nonummy nibh ligula pulvinar metus eget consectetuer augue nisi quis lacus Ut ac mi quis lacus mollis aliquam Curabitur iaculis tempus <span style="font-size:20px;color:#888">”</span></p>
  <div class="abs center" style="left:0;top:3402px;width:1200px;font-size:12px;font-weight:600;color:var(--gold)">BY AUTHOR NAME</div>
</section>

<section class="newsletter">
  <h3 class="abs" style="left:128px;top:54px;color:#fff;font-size:19px;font-weight:600">SUSCRIBE OUR NEWSLETTER</h3>
  <p class="abs" style="left:128px;top:86px;width:380px;color:#aaa;font-size:13px;line-height:17px">Lorem Ipsum has been the industry's standard dummy text ever since the 1500s, when ans,.</p>
  <div class="abs" style="left:530px;top:64px;width:348px;height:43px;border:1px solid #888;color:#ccc;font-size:12px;padding:12px 20px">Email Adddres</div>
  <div class="btn" style="left:886px;top:64px;width:176px;height:43px;background:linear-gradient(90deg,#e4b940,#c9982a);color:#fff;font-size:12px">Suscribe</div>
</section>

<footer class="footer">
  <div class="abs" style="left:131px;top:108px;display:flex;align-items:center;gap:10px;color:var(--gold);font-size:24px;font-weight:600"><span style="width:18px;height:18px;border-radius:50%;background:var(--gold)"></span>Ironvale Locker</div>
  <div class="abs" style="left:397px;top:64px">
    <h4>Navigation</h4>
    <ul><li>Home</li><li>About Us</li><li>Products</li><li>Blogs</li><li>Contact Us</li></ul>
  </div>
  <div class="abs" style="left:646px;top:64px">
    <h4>Category</h4>
    <ul><li>Men's Jewelry</li><li>Cigar &amp; Bar Products</li><li>Man Cave Swag</li></ul>
  </div>
  <div class="abs" style="left:888px;top:64px">
    <h4>Contact Us</h4>
  </div>
  <svg class="abs" style="left:886px;top:112px" width="32" height="32"><circle cx="16" cy="16" r="15" fill="#d4a12a"/><path d="M11 9l3 0 1 4-2 1c1 2 3 4 5 5l1-2 4 1v3c-6 1-13-6-12-12z" fill="#fff"/></svg>
  <div class="abs" style="left:928px;top:112px;font-size:12px;line-height:18px;color:#ddd">Phone number<br>+123 4567890</div>
  <svg class="abs" style="left:886px;top:168px" width="32" height="32"><circle cx="16" cy="16" r="15" fill="#d4a12a"/><rect x="9" y="11" width="14" height="10" fill="#fff"/><path d="M9 11l7 6 7-6" fill="none" stroke="#d4a12a" stroke-width="1.3"/></svg>
  <div class="abs" style="left:928px;top:168px;font-size:12px;line-height:18px;color:#ddd">Email us<br>info@ironvalelocker.com</div>
  <div class="social" style="left:892px"></div>
  <div class="social" style="left:927px"></div>
  <div class="social" style="left:962px"></div>
  <div class="social" style="left:997px"></div>
  <div class="abs" style="left:131px;top:351px;width:1012px;height:1px;background:#3a3a3a"></div>
  <div class="abs" style="left:147px;top:373px;font-size:10.5px;color:#ccc">© 2023 Ironvale Locker. All Rights Reserved</div>
  <div class="abs" style="left:840px;top:373px;font-size:10.5px;color:#ccc;word-spacing:2px">Privacy Policy &nbsp;&nbsp; Terms&amp; Conditions &nbsp;&nbsp; Sitemap</div>
</footer>

</body>
</html>
```